Beer Sommelier Business Card

Dear Designers,
I'm looking forward a Beer Sommelier business card. I'm a Beer Sommelier and also a Chef in Rio de Janeiro, Brazil but this card has to be a Beer Sommelier card.
I do consulting, brigade training, tastings and harmonizations.
Forget about themes such as rock and roll, motorcycles, conventional English pubs and bellied beer drinkers. This business card will be delivered to restaurant owners and investors in Rio.
It has to seek elegance rather than luxury, and refinement rather than fashion.
I work using a black dress shirt, a Varnel Osterby watch and a 18k 1981 Dumelle aviator eyeglasses. I'm a business man and It's all part of the game.
Obviously, it has to be written in PORTUGUESE (only) and just as little as possible.

Informations to be included:

Tiago Varquim

Beer Sommelier
Chef de Cuisine

Consultoria
Treinamento de Brigada
Degustações
Harmonizações

telephone number (just numbers): 947261380

email (just the adress): tiagovarquim@mailnest.example

PS:
The letter "c" on both words "Degustações" and "Harmonizações" they have a small trace under it.
The letter "o" on both words "Degustações" and "Harmonizações" they have a small wave above it.

Blame the Latin.

Best Regards

Target Market(s)

Restaurant Owners and Investors. I have to impress them with my business card before I offer my services.

Industry/Entity Type

Restaurant

Contact Information for Business Card

An unique and well constructed Sommelier Business Card

Requirements
Must have
• A firts look impact. An unique and well made design. Not an ordinary product.
• Tiago Varquim
• Beer Sommelier/Chef de Cuisine
• Consultoria
• Treinamento de Brigada
• Degustações
• Harmonizações
• telephone number (just numbers): 947261380
• email (just the adress): tiagovarquim@mailnest.example
• PS:
• The letter "c" on both words "Degustações" and "Harmonizações" they have a small trace under it.
• The letter "o" on both words "Degustações" and "Harmonizações" they have a small wave above it.
Nice to have
• Elegance, Refinement.
• Should be a Pro Style good Looking card,
• Forget themes like beer, chef and cuisine,
• It could be a laser engraved, metal, stainless steel, PVC, Triplex, Smooth, Letterpress, all black or any other good idea.
Should not have
• Words like telephone, email, cartoon pics or glass pics.
• Should not be an ordinary card that I could download from the web or use a web program and easily make by my self.
• Just Portuguese words

```html
<!DOCTYPE html>
<html lang="pt">
<head>
<meta charset="utf-8">
<title>Tiago Varquim — Cartão de Visita</title>
<link rel="stylesheet" href="https://fonts.googleapis.com/css2?family=Lato:wght@400;700;900&display=swap">
<style>
  :root {
    --bg: #e9e6e1;
    --card-black: #0b0b0d;
    --card-ink: #141418;
    --glow-blue: #3a63e0;
    --glow-cyan: #4fd6ff;
    --violet: #2a2a7a;
    --text-white: #f2f2f4;
    --text-soft: #c9cbd4;
    --accent: #38c6e8;
    --faint: #26262b;
  }
  * { box-sizing: border-box; margin: 0; padding: 0; }
  html, body {
    width: 1200px; height: 1023px; overflow: hidden;
    background: var(--bg);
    font-family: "Lato", Arial, sans-serif;
  }
  .canvas { position: relative; width: 1200px; height: 1023px; }

  .card {
    position: absolute;
    border-radius: 4px;
    overflow: hidden;
    box-shadow: 0 14px 34px rgba(0,0,0,.28);
  }

  /* Front */
  .card-front {
    left: 50px; top: 120px; width: 680px; height: 390px;
    background:
      radial-gradient(ellipse 60% 40% at 20% 20%, rgba(74,110,230,.55), transparent 70%),
      radial-gradient(ellipse 50% 35% at 85% 75%, rgba(74,110,230,.5), transparent 70%),
      linear-gradient(160deg, #1c1c4a 0%, var(--card-black) 45%, #101030 100%);
  }
  .light-band {
    position: absolute;
    background:
      radial-gradient(ellipse 30% 90% at 30% 50%, rgba(255,255,255,.55), transparent 70%),
      linear-gradient(90deg, var(--violet), var(--glow-blue) 25%, var(--glow-cyan) 50%, var(--glow-blue) 75%, var(--violet));
    opacity: .85;
  }
  .light-band.upper { left: 0; top: 48px; width: 680px; height: 58px; }
  .light-band.lower { left: 340px; top: 290px; width: 340px; height: 58px; }

  .services {
    position: absolute; left: 36px; top: 138px;
    display: flex; gap: 20px;
    color: var(--text-white); font-size: 17px; font-weight: 400; letter-spacing: .3px;
  }
  .services li { list-style: none; padding-left: 8px; }
  .services li + li { border-left: 2px solid var(--accent); }
  .services li:first-child { padding-left: 0; }

  .identity {
    position: absolute; right: 40px; top: 184px; text-align: right;
  }
  .identity .name { color: var(--text-white); font-size: 21px; font-weight: 900; }
  .identity .role { color: var(--text-soft); font-size: 15px; margin-top: 2px; }

  .contact {
    position: absolute; left: 36px; top: 290px;
    color: var(--text-white); font-size: 15px; line-height: 1.4;
  }

  /* Back */
  .card-back {
    left: 790px; top: 330px; width: 360px; height: 630px;
    background: linear-gradient(180deg, var(--card-ink), var(--card-black));
  }
  .monogram-field {
    position: absolute; left: 20px; top: -60px; width: 330px; height: 330px;
    border-radius: 50%; background: var(--faint);
  }
  .back-name {
    position: absolute; left: 22px; bottom: 40px;
    writing-mode: vertical-rl;
    color: var(--text-white); font-size: 30px; font-weight: 900; letter-spacing: 1px;
  }
  .back-mark {
    position: absolute; right: 30px; bottom: 46px;
    display: flex; align-items: center; gap: 8px;
    color: var(--text-white); font-size: 16px; font-weight: 700;
  }
  .back-mark .dot { width: 14px; height: 14px; border-radius: 50%; background: var(--text-white); }
</style>
</head>
<body>
<div class="canvas">
  <section class="card card-front">
    <div class="light-band upper" role="img" aria-label="Faixa luminosa azul com listras pretas diagonais"></div>
    <div class="light-band lower" role="img" aria-label="Faixa luminosa azul com listras pretas diagonais"></div>
    <ul class="services">
      <li>Consultoria</li>
      <li>Degustações</li>
      <li>Harmonizações</li>
      <li>Treinamento de Brigada</li>
    </ul>
    <div class="identity">
      <div class="name">Tiago Varquim</div>
      <div class="role">Beer Sommelier</div>
      <div class="role">Chef de Cuisine</div>
    </div>
    <div class="contact">
      <div>947261380</div>
      <div>tiagovarquim@mailnest.example</div>
    </div>
  </section>

  <section class="card card-back">
    <div class="monogram-field" aria-hidden="true"></div>
    <div class="back-name">TIAGO VARQUIM</div>
    <div class="back-mark"><span class="dot"></span>Tiago Varquim</div>
  </section>
</div>
</body>
</html>
```